Tarrawick Football Netball Club - 2015 Sponsorship Packages

We are a local sporting club based in Tarrawick, Victoria Australia. We would like to attract potential sponsors to our club by making a professional and striking, double sided A3 cover document containing the information in the attached files.
The club colours blue, red and white and logo should be prominent, and all photos used.
Feel free to move text from the Sponsorship introductory letter and Membership packages files to suite layout & formatting.
Enjoy

Target Market(s)

Corporate and small business owners in local and Melbourne community

Industry/Entity Type

Club

Font styles to use
Serif

Colors
0255a3
ec2027
ffffff

Requirements
Must have
• 4 pages. 2 fold
Nice to have
• Use red white and blue colours, club logo, photos set behind text

```html
<!DOCTYPE html>
<html lang="en">
<head>
<meta charset="utf-8">
<title>Tarrawick 2015 Sponsorship Packages – Inside Spread</title>
<link rel="stylesheet" href="https://fonts.googleapis.com/css2?family=Archivo+Black&family=Roboto+Condensed:wght@400;700&family=Roboto+Slab:wght@700;800&display=swap">
<style>
  :root {
    --club-blue: #0255a3;
    --deep-blue: #0a3a8c;
    --night-blue: #072c6e;
    --club-red: #ec2027;
    --white: #ffffff;
    --ink: #2b2b2b;
    --kennel-tint: #fbd6c8;
    --pound-tint: #fdf5de;
    --watch-grey: #8e9196;
    --watch-tint: #e4e5e8;
    --top-gold: #e5a81f;
    --top-tint: #fdf1c8;
    --page-bg: #ffffff;
  }
  * { box-sizing: border-box; margin: 0; padding: 0; }
  html, body {
    width: 1200px; height: 848px; overflow: hidden;
    background: var(--page-bg);
    font-family: "Roboto Condensed", "Arial Narrow", sans-serif;
    color: var(--ink);
  }
  .spread {
    position: relative; width: 1200px; height: 848px; overflow: hidden;
    background: linear-gradient(180deg, var(--night-blue) 0, var(--club-blue) 110px, #5f86c4 175px, #d6deec 235px, #ffffff 300px, #ffffff 100%);
  }

  /* masthead */
  .club-mark {
    position: absolute; left: 40px; top: 20px; width: 76px; height: 76px;
    display: flex; align-items: center; justify-content: center; text-align: center;
    border-radius: 50%; background: var(--white);
  }
  .club-mark span { font-weight: 700; font-size: 10.5px; line-height: 1.1; color: var(--deep-blue); }
  .masthead {
    position: absolute; left: 150px; top: 32px;
    font-family: "Archivo Black", "Arial Black", sans-serif;
    color: var(--white); font-size: 35px; letter-spacing: 0.5px; white-space: nowrap;
  }
  .masthead .year { font-size: 50px; margin: 0 20px; vertical-align: -4px; }
  .intro {
    position: absolute; left: 34px; top: 104px; width: 570px;
    color: var(--white); font-size: 10.2px; line-height: 1.45;
  }

  /* packages */
  .package {
    position: absolute; z-index: 2; border-radius: 26px 26px 30px 30px;
    border: 3px solid var(--accent);
    background: linear-gradient(180deg, var(--tint) 0, #ffffff 75%);
    padding: 76px 12px 18px 14px;
    box-shadow: 0 2px 4px rgba(0,0,0,.25);
  }
  .package-head {
    position: absolute; left: -3px; right: -3px; top: -3px; height: 66px;
    border-radius: 26px 26px 6px 6px; background: var(--accent);
    border: 2px solid var(--white); box-shadow: 0 2px 3px rgba(0,0,0,.35);
    display: flex; flex-direction: column; align-items: center; justify-content: center;
    font-family: "Roboto Slab", Georgia, serif; font-weight: 800; color: var(--white);
    text-align: center; line-height: 1.1;
  }
  .package-head .name { font-size: 17px; }
  .package-head .role { font-size: 15px; letter-spacing: 0.5px; }
  .package ul { list-style: none; font-size: 9.6px; line-height: 1.4; }
  .package li { padding-left: 9px; text-indent: -9px; }
  .package li::before { content: "– "; }
  .package li.sub { padding-left: 22px; }
  .package .note {
    margin-top: 10px; text-align: center; font-weight: 700; font-size: 10px; line-height: 1.3; color: #111;
  }
  .deal { position: absolute; width: 66px; height: 66px; top: -34px; right: -22px; }
  .deal text { font-family: "Roboto Condensed", sans-serif; font-weight: 700; fill: var(--white); }

  .package--kennel { --accent: var(--club-red); --tint: var(--kennel-tint); left: 46px; top: 208px; width: 236px; }
  .package--pound { --accent: var(--club-blue); --tint: var(--pound-tint); left: 308px; top: 208px; width: 232px; }
  .package--watch { --accent: var(--watch-grey); --tint: var(--watch-tint); left: 620px; top: 126px; width: 218px; }
  .package--top { --accent: var(--top-gold); --tint: var(--top-tint); left: 856px; top: 126px; width: 298px; }
  .package--watch .package-head { background: linear-gradient(180deg, #b5b8bd, #7c8086); }
  .package--top .package-head { background: linear-gradient(180deg, #f3c54a, #d7951a); }
  .package--watch ul, .package--top ul { font-size: 9.4px; line-height: 1.36; }

  /* club stripes */
  .stripes { position: absolute; z-index: 1; left: 0; top: 650px; width: 1200px; height: 18px; }
  .stripes .red { height: 7px; background: var(--club-red); }
  .stripes .gap { height: 4px; background: var(--white); }
  .stripes .blue { height: 7px; background: var(--club-blue); }

  /* lower band */
  .lower-band {
    position: absolute; left: 0; top: 672px; width: 1200px; height: 176px;
    background: linear-gradient(180deg, var(--deep-blue), var(--night-blue));
    color: var(--white);
  }
  .benefits { position: absolute; left: 34px; top: 18px; width: 560px; font-size: 10px; line-height: 1.5; }
  .benefits h2 { font-size: 10.5px; font-weight: 400; margin-bottom: 8px; }
  .benefits ol { padding-left: 14px; }
  .ambition { position: absolute; left: 633px; top: 14px; width: 540px; font-size: 10px; line-height: 1.5; }
  .ambition p + p { margin-top: 8px; }
</style>
</head>
<body>
<main class="spread">

  <div class="club-mark"><span>Tarrawick<br>Football<br>Netball Club</span></div>
  <h1 class="masthead">Tarrawick<span class="year">2015</span>Sponsorship Packages</h1>

  <p class="intro">We have reviewed our sponsorship area and have identified as a club that we want to do more for our sponsors. Historically our sponsors have given generously without expecting too much in return. From 2015 we are committed to ensuring our sponsors feel valued, appreciated and that your sponsorship has return on investment benefits to cater for your individual business needs. This will be achieved through stronger patronage from club members and the community as well as a higher level of recognition and exposure for your business. In simple terms we want the club and our sponsors to feel a sense of connection and support for each other – a Win/Win for both parties.</p>

  <section class="package package--kennel">
    <div class="package-head"><span class="name">“The Kennel Club”</span><span class="role">SPONSORS</span></div>
    <svg class="deal" viewBox="0 0 66 66" aria-hidden="true">
      <polygon points="33,1 40,14 55,9 52,24 65,33 52,42 55,57 40,52 33,65 26,52 11,57 14,42 1,33 14,24 11,9 26,14" fill="#ec2027"/>
      <text x="33" y="32" text-anchor="middle" font-size="12">$1,000+</text>
      <text x="33" y="45" text-anchor="middle" font-size="11">DEAL</text>
    </svg>
    <ul>
      <li>Permanent fence sign around ground</li>
      <li>TFNC website advertising</li>
      <li>Advertising Signage in Function Room</li>
      <li>Business logo in club business directory</li>
      <li>TFNC Website advertising</li>
      <li>2 x Membership Tickets – Entry to home games</li>
      <li>2 x Admission to Half Time Bulldogs Club</li>
      <li>2 x 50% Discount off all away games</li>
      <li>2 x Tarrawick Bulldogs caps, key rings, stubby holders &amp; fridge magnet fixtures</li>
      <li>Free Tarrawick Bulldogs Mobile Phone App</li>
      <li>2 x Home Game Draw Ticket (chance of winning $1,000 every home game)</li>
      <li>2 x 2 people @ Sponsors dinners/functions</li>
      <li>4 x 2 people @ Thursday Night Selection Dinners</li>
      <li>1 x 2 people @ Game day experience</li>
      <li class="sub">seats in coaches box</li>
      <li>2 x TFNC “Bomber jackets”</li>
      <li>1 x Certificate of recognition/appreciation</li>
      <li>1 x framed TFNC team photo</li>
    </ul>
    <p class="note">N.B – To negotiate further benefits<br>appropriate to your business.</p>
  </section>

  <section class="package package--pound">
    <div class="package-head"><span class="name">“The Pound”</span><span class="role">SPONSORS</span></div>
    <svg class="deal" viewBox="0 0 66 66" aria-hidden="true">
      <polygon points="33,1 40,14 55,9 52,24 65,33 52,42 55,57 40,52 33,65 26,52 11,57 14,42 1,33 14,24 11,9 26,14" fill="#0255a3"/>
      <text x="33" y="32" text-anchor="middle" font-size="12">$2,500+</text>
      <text x="33" y="45" text-anchor="middle" font-size="11">DEAL</text>
    </svg>
    <ul>
      <li>Permanent fence sign around ground</li>
      <li>TFNC Website advertising</li>
      <li>Advertising Signage in Function Room</li>
      <li>Business logo in club business directory</li>
      <li>2 x Membership Tickets</li>
      <li class="sub">Entry to home games</li>
      <li>2 x Admission to Half Time Bulldogs Club</li>
      <li>2 x 50% Discount off all away games</li>
      <li>2 x Tarrawick Bulldogs caps, key rings, stubby holders &amp; fridge magnet fixtures</li>
      <li>Free Tarrawick Bulldogs Mobile Phone App</li>
      <li>2 x Home Game Draw Ticket (chance of winning $1,000 every home game)</li>
      <li>2 x 2 people @ Sponsors dinners/functions</li>
      <li>4 x 2 people @ Thursday Night Selection Dinners</li>
      <li>1 x 2 people @ Game day experience</li>
      <li class="sub">seats in coaches box</li>
      <li>2 x TFNC “Bomber jackets”</li>
      <li>1 x Certificate of recognition/appreciation</li>
      <li>1 x framed TFNC team photo</li>
    </ul>
    <p class="note">N.B – To negotiate further benefits<br>appropriate to your business.</p>
  </section>

  <section class="package package--watch">
    <div class="package-head"><span class="name">“Watch Dog”</span><span class="role">SPONSORS</span></div>
    <svg class="deal" viewBox="0 0 66 66" aria-hidden="true">
      <polygon points="33,1 40,14 55,9 52,24 65,33 52,42 55,57 40,52 33,65 26,52 11,57 14,42 1,33 14,24 11,9 26,14" fill="#9a9da3"/>
      <text x="33" y="32" text-anchor="middle" font-size="12">$5,000+</text>
      <text x="33" y="45" text-anchor="middle" font-size="11">DEAL</text>
    </svg>
    <ul>
      <li>Permanent fence sign around ground</li>
      <li>Advertising signage in function room</li>
      <li>Business logo in Club Business Directory</li>
      <li>TFNC website advertising</li>
      <li>4 x Membership Tickets</li>
      <li class="sub">Entry to home games</li>
      <li>4 x Admission to Half Time Bulldogs Club</li>
      <li>4 x 50% Discount off all away games</li>
      <li>4 x Tarrawick Bulldogs caps, key rings, stubby holders &amp; fridge magnets</li>
      <li>Free Tarrawick Bulldogs Mobile Phone App</li>
      <li>4 x Home Game Draw Tickets (chance of winning $1,000 every home game)</li>
      <li>4 x 4 people @ Thursday Night Selection Dinners</li>
      <li>4 people @ 2 x sponsor functions</li>
      <li>4 people @ 1 Game day experience</li>
      <li class="sub">(Coaches box)</li>
      <li>4 people @ 1 Game day experience</li>
      <li class="sub">(Pre and post game coaches address/debrief with players)</li>
      <li>1 x attendance at TFNC pre-season camp</li>
      <li>1 x framed TFNC team photo/recognition plaque</li>
      <li>4 x TFNC “Bomber jackets”</li>
    </ul>
    <p class="note">N.B – To negotiate further benefits<br>appropriate to your business.</p>
  </section>

  <section class="package package--top">
    <div class="package-head"><span class="name">“Top Dog”</span><span class="role">SPONSORS</span></div>
    <svg class="deal" viewBox="0 0 66 66" aria-hidden="true">
      <polygon points="33,1 40,14 55,9 52,24 65,33 52,42 55,57 40,52 33,65 26,52 11,57 14,42 1,33 14,24 11,9 26,14" fill="#e5a81f"/>
      <text x="33" y="32" text-anchor="middle" font-size="11">$10,000+</text>
      <text x="33" y="45" text-anchor="middle" font-size="11">DEAL</text>
    </svg>
    <ul>
      <li>Permanent fence sign around ground</li>
      <li>Advertising signage in Function Room</li>
      <li>Business logo in Club Business Directory</li>
      <li>TFNC website advertising</li>
      <li>4 x Membership Tickets – Entry to home games</li>
      <li>4 x Admission to Half Time Bulldogs Club</li>
      <li>4 x 50% Discount off all away games</li>
      <li>4 x Tarrawick Bulldogs caps, key rings, stubby holders &amp; fridge magnet fixtures</li>
      <li>Free Tarrawick Bulldogs Mobile Phone App</li>
      <li>4 x Home Game Draw Tickets (chance of winning $1000 every home game)</li>
      <li>4 x 6 people @ Thursday Night Selection Dinners</li>
      <li>6 people @ 2 x sponsor functions</li>
      <li>4 people @ 2 x Game day experience</li>
      <li class="sub">(Coaches box)</li>
      <li>6 people @ 2 x Game day experience</li>
      <li class="sub">(Pre and post game coaches address/debrief with players)</li>
      <li>4 people to have lunch or dinner with senior coach and captains of Football &amp; Netball teams and president of club</li>
      <li>2 people attendance at TFNC pre-season camp</li>
      <li>1 x large TFNC team photo/recognition plaque</li>
      <li>4 x TFNC “Bomber jackets”</li>
    </ul>
    <p class="note">N.B – To negotiate further benefits<br>appropriate to your business.</p>
  </section>

  <div class="stripes" aria-hidden="true"><div class="red"></div><div class="gap"></div><div class="blue"></div></div>

  <section class="lower-band">
    <div class="benefits">
      <h2>Further negotiation benefits include but not limited to;</h2>
      <ol>
        <li>Apparel sponsorship – Jumper, shorts, netball skirts, tracksuit tops, polo tops, warm up tops and training wear.</li>
        <li>Major structure sponsorship – New coaches box, scoreboard, pavilion, netball courts and lighting upgrades.</li>
        <li>Themed round sponsorship – Pink Day ladies day (breast cancer &amp; respect for women) and Heritage Round.</li>
        <li>Wind breakers for ¾ and ½ time break</li>
        <li>Patronage of your business where appropriate. Eg. Food and beverage for committee meetings, club social functions etc.</li>
        <li>Directing club members to your business for purchasing items or services wherever it is possible.</li>
      </ol>
    </div>
    <div class="ambition">
      <p>As a participant in the progressive and powerful Calder Ridge FNL we are striving to become the benchmark club in the competition, therefore we must continue to grow and improve to achieve our goal. We have exciting plans and projects underway to upgrade our facilities and resources for our football and netball players, members and supporters. These initiatives and projects commenced in 2014 as part of our strategic plan and will continue over the coming months and throughout 2015. We aim to provide the youth and players of our region every chance of becoming the best they can be. To achieve this, our strategic plan is to attract the best coaches and personnel within the Ridgeview Ranges.</p>
      <p>We are proud to give back to our community, particularly our youth. We not only want to create a successful club, we want to foster a community environment conducive to developing wonderful people.</p>
    </div>
  </section>

</main>
</body>
</html>
```